Residential Construction Business - Site Signage

I need a design made for a site fence banner. We have a logo and branding so the design would need to be aligned with this. It would need to be made to specific size ratio so that it can be sent to the maker for production.
ratio : 4600 wide x 1700 high
The design should feature our website and also the slogan
"don't move, re-imagine"

Target Market(s)

potential clients

Industry/Entity Type

construction

Font styles to use
Other font styles liked:
• to match branding

Colors
0054AA
0677BA
7BADD7
CADEEF
E8F1F8

Requirements
Must have
• www.velmbuild.com.au Majority of the sign is our brand logo
Nice to have
• Majority of the sign is our brand logo
Should not have
• colors and themes that arent brand relevant

```html
<!DOCTYPE html>
<html lang="en">
<head>
<meta charset="utf-8">
<title>Velm Build – Site Fence Banner</title>
<link href="https://fonts.googleapis.com/css2?family=Poppins:wght@500;600;700&family=Roboto+Condensed:wght@700&display=swap" rel="stylesheet">
<style>
  :root {
    --page-bg: #c0c8d0;
    --navy: #053b61;
    --navy-deep: #04304f;
    --light-panel-top: #f2f2f2;
    --light-panel-bottom: #d9d9d9;
    --white: #ffffff;
    --soft-white: #e2e2e2;
    --ink: #111111;
    --fold: #9aa3ab;
  }
  * { margin: 0; padding: 0; box-sizing: border-box; }
  html, body {
    width: 1093px;
    height: 1200px;
    overflow: hidden;
    background: var(--page-bg);
  }
  .banner {
    position: absolute;
    left: 92px;
    top: 432px;
    width: 910px;
    height: 336px;
    overflow: hidden;
    box-shadow: 0 6px 18px rgba(0, 0, 0, 0.35);
  }
  .site-photo {
    position: absolute;
    inset: 0;
    background: linear-gradient(160deg, var(--light-panel-top) 0%, #e4e4e4 55%, var(--light-panel-bottom) 100%);
  }
  .slogan-panel {
    position: absolute;
    left: 0;
    top: 0;
    width: 409px;
    height: 336px;
    background: linear-gradient(180deg, var(--navy) 0%, var(--navy-deep) 100%);
  }
  .slogan {
    position: absolute;
    left: 36px;
    top: 50px;
    font-family: "Poppins", sans-serif;
    font-weight: 700;
    color: var(--white);
    line-height: 0.92;
    letter-spacing: -0.02em;
  }
  .slogan-main { display: block; font-size: 101px; }
  .slogan-sub {
    display: block;
    margin-top: 10px;
    font-size: 55px;
    font-weight: 600;
    color: var(--soft-white);
    letter-spacing: -0.01em;
  }
  .brand-block {
    position: absolute;
    left: 432px;
    top: 21px;
    width: 199px;
    height: 199px;
    background: var(--navy);
  }
  .brand-name {
    position: absolute;
    left: 650px;
    top: 102px;
    font-family: "Poppins", sans-serif;
    font-weight: 600;
    font-size: 26px;
    letter-spacing: 0.22em;
    color: var(--navy);
    white-space: nowrap;
  }
  .web-strip {
    position: absolute;
    left: 384px;
    top: 246px;
    width: 526px;
    height: 54px;
    background: var(--white);
    display: flex;
    align-items: center;
    justify-content: center;
    box-shadow: 0 3px 6px rgba(0, 0, 0, 0.18);
  }
  .web-strip-fold {
    position: absolute;
    left: 384px;
    top: 300px;
    width: 25px;
    height: 10px;
  }
  .web-address {
    font-family: "Roboto Condensed", sans-serif;
    font-weight: 700;
    font-size: 44px;
    line-height: 1;
    color: var(--ink);
    letter-spacing: -0.01em;
  }
</style>
</head>
<body>
  <section class="banner">
    <div class="site-photo" role="img" aria-label="Faded photograph of building scaffolding against a pale sky"></div>

    <div class="slogan-panel">
      <h1 class="slogan">
        <span class="slogan-main">DON'T</span>
        <span class="slogan-main">MOVE,</span>
        <span class="slogan-sub">RE-IMAGINE</span>
      </h1>
    </div>

    <div class="brand-block" aria-hidden="true"></div>
    <div class="brand-name">VELM BUILD</div>

    <svg class="web-strip-fold" viewBox="0 0 25 10" aria-hidden="true">
      <polygon points="0,0 25,0 25,10" fill="var(--fold)"/>
    </svg>
    <div class="web-strip">
      <span class="web-address">www.velmbuild.com.au</span>
    </div>
  </section>
</body>
</html>
```